Lip Balm Label Design

Design a label for a Lavender-Mint lip balm. We make high-quality natural essential oil products. Please use the old label as an example of what exists. The label should include purple. The final design should be eye-catching and distinct. The file should be in an AI file.

Here is the information that should be included on the label:
1) ingredients:Theobroma Cacao (Cocoa) Seed Butter, Theobroma grandiflorum Ultra Refined Butter, beesewax, Calendula Officinalis Flower Oil, Prunus Amygdalus Dulcis (Sweet Almond) Oil, cetyl alcohol and Tocopherol. Lavandula Angustifolia (Lavender) Oil and Mentha Piperita (Peppermint) Oil.

2) www.kelvorascents.com

3) Brand name and logo: K. Velora Aromatherapy (logo is attached- you can use with form)

```html
<!DOCTYPE html>
<html lang="en">
<head>
<meta charset="utf-8">
<title>Lavender-Mint Lip Balm Label</title>
<link href="https://fonts.googleapis.com/css2?family=Fraunces:opsz,wght@9..144,500;9..144,600&family=Mulish:wght@500;600&display=swap" rel="stylesheet">
<style>
  :root {
    --page-bg: #ebebeb;
    --panel-bg: #f6e7f8;
    --tube-light: #e6d7e9;
    --tube-mid: #d2c1d6;
    --tube-dark: #b6a5ba;
    --ink: #6a2447;
    --lavender: #8f7fb3;
    --leaf: #8bab6a;
  }
  * { margin: 0; padding: 0; box-sizing: border-box; }
  html, body {
    width: 1200px;
    height: 960px;
    overflow: hidden;
    background: var(--page-bg);
  }
  .canvas {
    position: relative;
    width: 1200px;
    height: 960px;
  }
  .label {
    position: absolute;
    left: 222px;
    top: 71px;
    width: 756px;
    height: 818px;
    display: flex;
  }
  .panel { position: relative; height: 100%; }

  /* Left: product claims */
  .panel-claims {
    width: 124px;
    background: var(--panel-bg);
  }
  .claims {
    position: absolute;
    left: 50%;
    bottom: 66px;
    transform: translateX(-50%) rotate(180deg);
    writing-mode: vertical-rl;
    font-family: "Mulish", sans-serif;
    font-weight: 600;
    font-size: 20.5px;
    line-height: 30px;
    color: var(--ink);
    white-space: nowrap;
    text-align: left;
  }

  /* Centre: front face */
  .panel-front {
    width: 304px;
    background: linear-gradient(90deg, var(--tube-light) 0%, var(--tube-mid) 30%, var(--tube-light) 52%, var(--tube-dark) 82%, var(--tube-mid) 100%);
  }
  .product-title {
    position: absolute;
    left: 50%;
    bottom: 196px;
    transform: translateX(-50%) rotate(180deg);
    writing-mode: vertical-rl;
    font-family: "Fraunces", serif;
    font-weight: 600;
    font-size: 70px;
    line-height: 76px;
    letter-spacing: -0.5px;
    color: var(--ink);
    white-space: nowrap;
  }
  .lavender-sprig {
    position: absolute;
    left: 44px;
    top: 658px;
    width: 214px;
    height: 118px;
  }

  /* Right: brand & ingredients */
  .panel-info {
    width: 328px;
    background: var(--panel-bg);
    text-align: center;
    color: var(--ink);
    font-family: "Mulish", sans-serif;
  }
  .brand {
    position: absolute;
    top: 64px;
    left: 0;
    right: 0;
    display: flex;
    align-items: center;
    justify-content: center;
    gap: 7px;
  }
  .brand-dot {
    width: 12px;
    height: 12px;
    border-radius: 50%;
    background: var(--ink);
  }
  .brand-name {
    font-family: "Mulish", sans-serif;
    font-weight: 600;
    font-size: 15px;
    color: var(--ink);
  }
  .ingredients {
    position: absolute;
    top: 146px;
    left: 12px;
    right: 12px;
    font-weight: 600;
    font-size: 16px;
    line-height: 21.3px;
    letter-spacing: -0.2px;
  }
  .net-weight {
    position: absolute;
    top: 352px;
    left: 0;
    right: 0;
    font-weight: 500;
    font-size: 15px;
  }
</style>
</head>
<body>
<div class="canvas">
  <div class="label">
    <section class="panel panel-claims">
      <p class="claims">Organic essential oils| 100% Natural Ingredients | Gluten-Free|<br>Hopping Hare Certified | Paraben &amp; Sulfate Free</p>
    </section>

    <section class="panel panel-front">
      <h1 class="product-title">Lavender-Mint<br>Lip Balm</h1>
      <svg class="lavender-sprig" role="img" aria-label="Illustration of a lavender sprig with green leaves" viewBox="0 0 214 118">
        <defs>
          <linearGradient id="sprig-tone" x1="0" y1="0" x2="1" y2="0">
            <stop offset="0" stop-color="#9d8fc0"/>
            <stop offset="0.65" stop-color="#a79bc6"/>
            <stop offset="1" stop-color="#9cb883"/>
          </linearGradient>
        </defs>
        <rect width="214" height="118" rx="10" fill="url(#sprig-tone)" opacity="0.55"/>
      </svg>
    </section>

    <section class="panel panel-info">
      <div class="brand">
        <span class="brand-dot"></span>
        <span class="brand-name">K. Velora Aromatherapy</span>
      </div>
      <p class="ingredients">ingredients:Theobroma Cacao (Cocoa) Seed Butter, Theobroma grandiflorum Ultra Refined Butter, beesewax, Calendula Officinalis Flower Oil, Prunus Amygdalus Dulcis (Sweet Almond) Oil, cetyl alcohol and Tocopherol. Lavandula Angustifolia (Lavender) Oil and Mentha Piperita (Peppermint) Oil.</p>
      <p class="net-weight">0,15 oz (4.4 MLS)</p>
    </section>
  </div>
</div>
</body>
</html>
```